Flyer-Design für Vermittlung von Büromaschinen
Zielgruppe
Wir vertreiben Büromaschinen hauptsächlich hochwertige Kopierautomaten für Büros, Steuerberater, Rechtsanwälte usw.
Besonderen Augenmerk auf gebrauchte, generalüberholte Maschinen zur Miete an den Kunden, damit die Rohstoffe möglichst lange genutzt werden um die Umwelt zu schonen. zum Beispiel:
Willkommen in der Wegwerfgesellschaft.
Früher oder später wird alles weggeworfen. In der Konsumgesellschaft wandern aber auch gebrauchsfertige und neuwertige Produkte auf den Müll. Dieses hat fatale Konsequenzen: Klimawandel, Artensterben, Wassermangel- schon heute für viele existenzbedrohend. So wie wir wirtschaften, kann es nicht weitergehen! Wir müssen Rohstoffe möglichst lange nutzen, um dadurch die Umwelt zu schonen, denn wenn wir so weitermachen wie bisher werden 2050 mehr Plastik in unseren Ozeanen schwimmen als Fische. Helfen Sie uns beim Aufbau einer erfolgreichen Nutzungsform, bei der funktionstüchtige Kopierautomaten weiterhin eingesetzt werden sodass sichergestellt wird das Rohstoffe möglichst lange genutzt werden, um dadurch die Umwelt zu schonen. Bitte beachten Sie unser beigefügtes Angebot damit die Nachhaltigkeit gewinnt.
Wir kaufen gebrauchte Kopierautomaten von Leasinggesellschaften und bereiten diese in unserer Werkstatt auf. Diese dann neuwertigen, funktionstüchtigen Maschinen sollen dann vermietet werden.
Aufgabenstellung
Wir benötigen einen Flyer und ein entsprechendes Anschreiben.
Bilder und Texte können von der Website entnommen werden:
https://www.lummerich-buerotechnik.de/
Bei Anfrage kann ich Ihnen auch gerne die Bilder zur Verfügung stellen.
Bezüglich der Texte, würde ich mich auch über Vorschläge von Ihrer Seite freuen.

```html
<!DOCTYPE html>
<html lang="de">
<head>
<meta charset="utf-8">
<title>Flyer – Nachhaltig wirtschaften</title>
<link rel="stylesheet" href="https://fonts.googleapis.com/css2?family=Didact+Gothic&family=Exo+2:ital,wght@1,800&family=Oswald:wght@300&display=swap">
<style>
  :root {
    --teal: #6cc3bf;
    --ink: #555a5e;
    --navy: #1f2a6b;
    --paper: #ffffff;
    --stage: #e9eaeb;
    --photo-dark: #3a3c3f;
    --photo-light: #d9dadb;
  }
  * { box-sizing: border-box; margin: 0; padding: 0; }
  html, body { width: 1200px; height: 552px; overflow: hidden; }
  body {
    background: var(--stage);
    font-family: "Didact Gothic", sans-serif;
    color: var(--ink);
    position: relative;
  }
  .page {
    position: absolute;
    top: 36px;
    width: 480px;
    height: 480px;
    background: var(--paper);
    overflow: hidden;
    box-shadow: 0 4px 14px rgba(0,0,0,.18);
  }
  .page--front { left: 60px; }
  .page--back { left: 660px; }

  .band {
    position: absolute;
    left: 0; right: 0; bottom: 0;
    height: 40px;
    background: var(--teal);
    color: #fff;
    font-family: "Oswald", sans-serif;
    font-weight: 300;
    font-size: 17px;
    letter-spacing: 2.2px;
    display: flex;
    align-items: center;
    justify-content: center;
    white-space: nowrap;
  }

  /* Front */
  .printer-photo {
    position: absolute;
    left: 0; top: 0;
    width: 300px; height: 440px;
    background: linear-gradient(160deg, var(--photo-dark) 0%, var(--photo-dark) 42%, var(--photo-light) 43%, #f1f1f1 100%);
  }
  .earth-photo {
    position: absolute;
    left: 102px; top: 205px;
    width: 160px; height: 160px;
    border-radius: 50%;
    background: radial-gradient(circle at 40% 40%, #8aa57a 0%, #4f7f8a 45%, #1f3f6a 100%);
  }
  .headline {
    position: absolute;
    font-family: "Exo 2", sans-serif;
    font-style: italic;
    font-weight: 800;
    color: var(--teal);
    text-transform: uppercase;
    line-height: 1.12;
    font-size: 17px;
    letter-spacing: .5px;
  }
  .headline--top { left: 238px; top: 82px; }
  .headline--bottom { left: 262px; top: 200px; }
  .brand {
    position: absolute;
    left: 262px; top: 352px;
    font-size: 40px;
    color: var(--navy);
    letter-spacing: 1px;
  }

  /* Back */
  .back-title {
    position: absolute;
    left: 28px; top: 22px;
    font-size: 17px;
    font-weight: 400;
    color: var(--teal);
    letter-spacing: .3px;
    text-transform: uppercase;
  }
  .columns {
    position: absolute;
    left: 28px; right: 28px;
    display: grid;
    grid-template-columns: 1fr 1fr;
    column-gap: 20px;
    font-size: 10.5px;
    line-height: 1.45;
    letter-spacing: .3px;
  }
  .columns--intro { top: 50px; }
  .columns--outro { top: 330px; }
  .help-title {
    font-size: 16px;
    font-weight: 400;
    color: var(--teal);
    text-transform: uppercase;
    margin-bottom: 3px;
  }
  .cycle { position: absolute; left: 0; top: 110px; width: 480px; height: 210px; }
  .cycle svg { position: absolute; left: 0; top: 0; }
  .device { position: absolute; border-radius: 3px; }
  .device--mfp { left: 152px; top: 32px; width: 56px; height: 118px; background: linear-gradient(180deg,#bfc2c5,#eeeeee); }
  .device--office { left: 222px; top: 52px; width: 82px; height: 88px; background: linear-gradient(180deg,#3e4144,#1f2124); }
  .device--compact { left: 318px; top: 72px; width: 70px; height: 52px; background: linear-gradient(180deg,#e4e5e6,#c9cacc); }
  .step {
    position: absolute;
    font-size: 10.5px;
    line-height: 1.3;
    color: var(--ink);
    display: flex;
    align-items: center;
    gap: 6px;
    white-space: nowrap;
  }
  .step b { font-weight: 400; font-size: 22px; }
  .step--one { left: 22px; top: 88px; text-align: center; }
  .step--two { left: 250px; top: 2px; }
  .step--three { left: 330px; top: 128px; text-align: center; }
  .slogan {
    position: absolute;
    left: 162px; top: 150px;
    width: 130px;
    font-family: "Exo 2", sans-serif;
    font-style: italic;
    font-weight: 800;
    color: var(--teal);
    text-transform: uppercase;
    text-align: center;
    font-size: 12px;
    line-height: 1.2;
    letter-spacing: 1px;
  }
  .contact {
    position: absolute;
    left: 28px; top: 410px;
    font-size: 10px;
    line-height: 1.4;
    letter-spacing: .4px;
  }
</style>
</head>
<body>

<section class="page page--front">
  <div class="printer-photo" role="img" aria-label="Foto eines Bürodruckers mit Bedienfeld und ausgegebenem Blatt"></div>
  <div class="earth-photo" role="img" aria-label="Foto der Erdkugel auf dem Papierblatt"></div>
  <h1 class="headline headline--top">Helfen Sie uns,<br>nachhaltig<br>zu wirtschaften …</h1>
  <p class="headline headline--bottom">… denn<br>unser Planet<br>lässt sich<br>nicht kopieren!</p>
  <div class="brand">lummerich</div>
  <div class="band">+++ VERMIETUNG NEUWERTIGER GEBRAUCHTGERÄTE +++</div>
</section>

<section class="page page--back">
  <h2 class="back-title">Früher oder später wird alles weggeworfen</h2>
  <div class="columns columns--intro">
    <p>In unserer Konsumgesellschaft wandern aber auch gebrauchsfertige und neuwertige Produkte auf dem Müll. Dieses hat fatale Konsequenzen:</p>
    <p>Klimawandel, Artensterben, Wassermangel. So wie wir wirtschaften, kann es nicht weitergehen! Helfen Sie uns, Rohstoffe möglichst lange zu nutzen.</p>
  </div>

  <div class="cycle">
    <svg width="480" height="210" viewBox="0 0 480 210" aria-hidden="true">
      <g fill="none" stroke="var(--teal)" stroke-width="7" stroke-linecap="round">
        <path d="M94 76 C86 48 108 28 136 30"/>
        <path d="M352 12 C378 18 390 38 382 54"/>
        <path d="M112 146 C114 166 132 176 152 172"/>
        <path d="M352 178 C354 196 336 204 316 200"/>
      </g>
      <g fill="var(--teal)">
        <path d="M134 19 L149 30 L134 41 Z"/>
        <path d="M371 52 L382 67 L393 54 Z"/>
        <path d="M149 161 L163 171 L151 183 Z"/>
        <path d="M318 189 L304 199 L318 210 Z"/>
      </g>
    </svg>
    <div class="device device--mfp" role="img" aria-label="Foto eines großen Multifunktionskopierers"></div>
    <div class="device device--office" role="img" aria-label="Foto eines Büro-Kopiersystems mit Finisher"></div>
    <div class="device device--compact" role="img" aria-label="Foto eines kompakten Laserdruckers"></div>
    <div class="step step--one"><b>1</b><span>Ankauf<br>gebrauchter<br>Leasing-Geräte</span></div>
    <div class="step step--two"><b>2</b><span>Aufbereitung<br>in unserer<br>Werkstatt</span></div>
    <div class="step step--three"><span>Vermietung dieser<br>neuwertigen<br>Geräte</span><b>3</b></div>
    <p class="slogan">Gemeinsam<br>wirtschaften<br>wir nachhaltig</p>
  </div>

  <div class="columns columns--outro">
    <div>
      <h3 class="help-title">Helfen Sie mit …</h3>
      <p>… beim Aufbau einer erfolgreichen Nutzungsform, bei der funktionstüchtige Kopierautomaten weiterhin</p>
    </div>
    <p>eingesetzt werden sodass sichergestellt wird, daß Rohstoffe möglichst lange genutzt werden, um dadurch die Umwelt zu schonen.</p>
  </div>

  <p class="contact">lummerich Büro- und KopierSysteme GmbH, Keplerweg 8, 50999 Musterstadt<br>02200 – 12 34 56, info@lummerich-buerotechnik.de, www.lummerich-buerotechnik.de</p>

  <div class="band">+++ BITTE BEACHTEN SIE UNSER BEIGEFÜGTES ANGEBOT +++</div>
</section>

</body>
</html>
```